Pemberton Dialworks Business Card Design

Double Sided Business Card Design for a Locksmith company specializing in Safecracking, safe & vault service.

```html
<!DOCTYPE html>
<html lang="en">
<head>
<meta charset="utf-8">
<title>Pemberton Dialworks Business Card</title>
<link href="https://fonts.googleapis.com/css2?family=Lato:wght@400;700;900&display=swap" rel="stylesheet">
<style>
  :root {
    --bg: #a3a3a3;
    --green: #2e7d3c;
    --ink: #111111;
    --grey-text: #555555;
    --card-white: #ffffff;
    --card-black: #000000;
    --faint: #f4f5f1;
  }
  * { margin: 0; padding: 0; box-sizing: border-box; }
  html, body { width: 1200px; height: 1200px; overflow: hidden; }
  body { background: var(--bg); font-family: "Lato", sans-serif; position: relative; }

  .card {
    position: absolute;
    left: 198px;
    width: 806px;
    height: 460px;
    border-radius: 30px;
    overflow: hidden;
  }
  .card-front { top: 110px; background: var(--card-white); }
  .card-back { top: 616px; background: var(--card-black); left: 201px; width: 803px; }

  .faint-disc {
    position: absolute;
    left: 372px; top: 0;
    width: 470px; height: 470px;
    border-radius: 50%;
    background: var(--faint);
  }

  .brand { position: absolute; display: flex; align-items: center; }
  .brand-mark { border-radius: 50%; background: var(--green); flex: none; }
  .brand-name {
    font-family: "Lato", sans-serif;
    font-weight: 900;
    color: var(--green);
    text-transform: uppercase;
    line-height: 1;
  }
  .brand-name span { display: block; }

  .card-front .brand { left: 51px; top: 51px; }
  .card-front .brand-mark { width: 118px; height: 118px; margin-right: 24px; }
  .card-front .brand-name { font-size: 40px; letter-spacing: 0.5px; }
  .card-front .brand-name span + span { margin-top: 6px; }

  .card-back .brand { left: 106px; top: 146px; }
  .card-back .brand-mark { width: 180px; height: 180px; margin-right: 26px; }
  .card-back .brand-name { font-size: 58px; letter-spacing: 1px; }
  .card-back .brand-name span + span { margin-top: 8px; }

  .person { position: absolute; left: 51px; top: 240px; }
  .person-name { font-weight: 700; font-size: 28px; color: var(--green); line-height: 1.1; }
  .person-role { font-size: 19px; color: var(--grey-text); margin-top: 2px; }

  .contacts { position: absolute; left: 51px; top: 320px; list-style: none; }
  .contacts li {
    display: flex; align-items: center;
    font-size: 18px; color: var(--grey-text);
    height: 23.5px;
    white-space: nowrap;
  }
  .contacts li svg { width: 14px; height: 14px; margin: 0 14px 0 2px; fill: var(--green); flex: none; }

  .divider {
    position: absolute; left: 352px; top: 368px;
    width: 1.5px; height: 40px; background: #777;
  }
  .address { position: absolute; left: 368px; top: 362px; display: flex; }
  .address svg { width: 12px; height: 16px; fill: var(--green); margin: 4px 10px 0 0; flex: none; }
  .address p { font-size: 19px; color: var(--grey-text); line-height: 24px; white-space: nowrap; }

  .web-line {
    position: absolute; left: 0; right: 0; top: 394px;
    text-align: center;
    font-size: 17px; letter-spacing: 3.5px;
    color: #ffffff;
  }
  .web-line .web-domain { color: var(--green); }
</style>
</head>
<body>

  <section class="card card-front" aria-label="Business card front">
    <div class="faint-disc"></div>

    <div class="brand">
      <div class="brand-mark"></div>
      <div class="brand-name"><span>Pemberton</span><span>Dialworks</span></div>
    </div>

    <div class="person">
      <div class="person-name">Loren Ashcombe</div>
      <div class="person-role">Co-founder</div>
    </div>

    <ul class="contacts">
      <li>
        <svg viewBox="0 0 16 16"><path d="M3.5 1l2.5 3-1.5 2c.8 1.8 2.2 3.2 4 4l2-1.5 3 2.5-1.5 2.5C7 13.5 2.5 9 1 3.5z"/></svg>
        +1.555.920.6220
      </li>
      <li>
        <svg viewBox="0 0 16 16"><path d="M1 6c0-2 3-3 7-3s7 1 7 3v1h-3.5V5.5h-7V7H1zM3 8h10l1 5H2z"/></svg>
        +1.555.721.4299
      </li>
      <li>
        <svg viewBox="0 0 16 16"><path d="M1 3h14v1.5L8 9 1 4.5zM1 6.3l7 4.5 7-4.5V13H1z"/></svg>
        hi@pembertondialworks.com
      </li>
      <li>
        <svg viewBox="0 0 16 16"><circle cx="8" cy="8" r="7"/></svg>
        www.pembertondialworks.com
      </li>
    </ul>

    <div class="divider"></div>

    <div class="address">
      <svg viewBox="0 0 12 16"><path d="M6 0a6 6 0 0 1 6 6c0 4-6 10-6 10S0 10 0 6a6 6 0 0 1 6-6zm0 3.5a2.5 2.5 0 1 0 0 5 2.5 2.5 0 0 0 0-5z"/></svg>
      <p>4410 Harlow Lane,<br>Suite 17-21.</p>
    </div>
  </section>

  <section class="card card-back" aria-label="Business card back">
    <div class="brand">
      <div class="brand-mark"></div>
      <div class="brand-name"><span>Pemberton</span><span>Dialworks</span></div>
    </div>

    <p class="web-line">www.<span class="web-domain">pembertondialworks</span>.com</p>
  </section>

</body>
</html>
```